eBook and paperback cover

I need an eBook cover (planned release via Brindlemark and Qualto) and subsequently also a paperback cover (planned release via Telpuni), which looks appealing even in black and white and small format and reflects the following novel content.

The text consists of about 420 standard pages - how many pages the paperback will have in the end, I cannot say at the moment. Thus the cover should be designed in a way that the thickness of the spine can be adjusted by me if necessary. Please also take necessary crop margins into account with regard to the paperback cover.

Book title: Das Fenster, hinter dem kein Licht brennt
Author: Marlene Quistorf
Untertitel: Roman

General information about the content:

The core theme of the story is jealousy and self-identity: Emma, the main character (= 18 years old, long brown hair, brown eyes, pretty), finds out that her sister Céline (= 18 years old, dark-blond hair, brown-green eyes, thin) that is at the same age, lives the life of her dreams. Later she finds out, that her sisters life is not the way she imagined in the beginning – nothing is, what it seems to be.

Other relevant characters are Ferdinand (father of Emma and Céline), his friend and business partner Karl) and Emmas mother, the maid (Ekaterina).

The novel takes place in Vienna (Austria).

Blurb:

When Emma surprisingly finds out that she is adopted and is supposed to be the daughter of the wealthy Austrian Ferdinand and his maid Ekaterina, she scents a chance to escape her miserable life. Full of hope she travels to Vienna, where she experiences a bitter disappointment: Her father is anything but happy to see her, Ekaterina in not there and her half-sister Céline, who is the same age, seems to be living the life of her dreams.

But it was to get even worse: Back at home, Emma gradually slipped away from everything she had clung to in life. In her desperation, she is angry at her father, whom she blames for her fate, and jealous of her half-sister. In her quest for retribution, Emma becomes entangled in a maelstrom of intrigue that is set to change her life forever and put her understanding of justice to the test.

Target Market(s)

Women (age 28-65)

Colors
d3a5cc
b8a6cd
eea4c8
f59195
fabb94
fbc994
85acd3
fbf289

Requirements
Must have
• ebook cover (brindlemark standard size) and paperback cover (DIN A5)
Nice to have
• Colors as selected below (but please not all of them)

```html
<!DOCTYPE html>
<html lang="en">
<head>
<meta charset="utf-8">
<title>Das Fenster, hinter dem kein Licht brennt – Cover</title>
<link href="https://fonts.googleapis.com/css2?family=Yellowtail&family=Mulish:wght@400;500&display=swap" rel="stylesheet">
<style>
  :root {
    --coral: #f4898f;
    --coral-light: #f7a9ad;
    --blush: #f8d6d8;
    --sky: #85acd3;
    --sky-light: #b7cbe4;
    --navy: #1d3a7e;
    --ink: #141a5a;
    --white: #ffffff;
  }
  * { margin: 0; padding: 0; box-sizing: border-box; }
  html, body { width: 1200px; height: 831px; overflow: hidden; background: var(--white); }
  .cover {
    position: relative; width: 1200px; height: 831px; overflow: hidden;
    background: var(--coral);
    font-family: "Mulish", Arial, sans-serif;
  }
  .cover-photo {
    position: absolute; inset: 0;
    background:
      radial-gradient(ellipse 520px 300px at 930px 230px, rgba(255,255,255,.7), rgba(255,255,255,0) 70%),
      linear-gradient(155deg, rgba(244,137,143,0) 0%, rgba(244,137,143,0) 40%, rgba(246,182,190,.9) 52%, rgba(200,196,222,.95) 68%, var(--sky) 88%);
  }
  .cover-photo::after {
    content: ""; position: absolute; left: 420px; top: 380px; width: 780px; height: 451px;
    background: radial-gradient(ellipse at 70% 60%, rgba(120,160,205,.55), rgba(255,255,255,.25) 55%, rgba(255,255,255,0) 75%);
  }
  .back-glow {
    position: absolute; left: 60px; top: 20px; width: 430px; height: 240px;
    background: radial-gradient(ellipse at center, rgba(255,255,255,.95) 0%, rgba(255,255,255,.55) 40%, rgba(255,255,255,0) 70%);
  }
  .title {
    position: absolute; font-family: "Yellowtail", "Brush Script MT", cursive;
    font-weight: 400; color: var(--navy); white-space: nowrap;
    line-height: .9; transform: rotate(-12deg); transform-origin: left top;
  }
  .title span { display: block; }
  .title--back { left: 150px; top: 140px; font-size: 46px; }
  .title--back .l2 { padding-left: 55px; font-size: 36px; }
  .title--back .l3 { padding-left: 90px; font-size: 36px; }
  .title--front {
    left: 712px; top: 200px; font-size: 62px;
    text-shadow: 0 0 2px #fff, 0 0 3px #fff, 2px 2px 0 #fff;
  }
  .title--front .l2 { padding-left: 70px; font-size: 48px; }
  .title--front .l3 { padding-left: 120px; font-size: 48px; }
  .blurb {
    position: absolute; left: 68px; top: 272px; width: 465px;
    font-size: 11.6px; line-height: 13.6px; color: var(--ink); text-align: justify;
  }
  .blurb p + p { margin-top: 13px; }
  .quote { position: absolute; color: var(--white); font-size: 15px; line-height: 20px; }
  .quote--one { left: 78px; top: 490px; }
  .quote--one .q2 { padding-left: 53px; }
  .quote--one .by { padding-left: 179px; }
  .quote--two { left: 134px; top: 603px; }
  .quote--two .by { padding-left: 108px; }
  .website { position: absolute; left: 52px; top: 773px; font-size: 14px; color: var(--ink); }
  .spine { position: absolute; left: 593px; top: 0; width: 32px; height: 831px; }
  .spine-title, .spine-author {
    position: absolute; left: 50%; white-space: nowrap;
    transform: translate(-50%, -50%) rotate(-90deg);
  }
  .spine-title { top: 205px; font-family: "Yellowtail", "Brush Script MT", cursive; font-size: 20px; color: var(--navy); }
  .spine-author { top: 672px; font-size: 23px; color: var(--ink); letter-spacing: .5px; }
  .author-front { position: absolute; left: 800px; top: 762px; font-size: 25px; color: var(--ink); }
</style>
</head>
<body>
<main class="cover">
  <div class="cover-photo" role="img" aria-label="Photograph: two young women with windswept hair in a Vienna street, toned in coral and blue"></div>
  <div class="back-glow"></div>

  <h2 class="title title--back"><span class="l1">Das Fenster,</span><span class="l2">hinter dem</span><span class="l3">kein Licht brennt</span></h2>

  <section class="blurb">
    <p>When Emma surprisingly finds out that she is adopted and is supposed to be the daughter of the wealthy Austrian Ferdinand and his maid Ekaterina, she scents a chance to escape her miserable life. Full of hope she travels to Vienna, where she experiences a bitter disappointment: Her father is anything but happy to see her, Ekaterina in not there and her half-sister Céline, who is the same age, seems to be living the life of her dreams.</p>
    <p>But it was to get even worse: Back at home, Emma gradually slipped away from everything she had clung to in life. In her desperation, she is angry at her father, whom she blames for her fate, and jealous of her half-sister. In her quest for retribution, Emma becomes entangled in a maelstrom of intrigue that is set to change her life forever and put her understanding of justice to the test.</p>
  </section>

  <blockquote class="quote quote--one">
    <div>"A great and shocking story</div>
    <div class="q2">of jealousy and self-identity"</div>
    <div class="by">- Name Surname</div>
  </blockquote>
  <blockquote class="quote quote--two">
    <div>“Nothing is, what it seems to be”</div>
    <div class="by">- Name Surname</div>
  </blockquote>

  <p class="website">www.marlenequistorf.com</p>

  <div class="spine">
    <span class="spine-title">Das Fenster, hinter dem kein Licht brennt</span>
    <span class="spine-author">Marlene Quistorf</span>
  </div>

  <h1 class="title title--front"><span class="l1">Das Fenster,</span><span class="l2">hinter dem</span><span class="l3">kein Licht brennt</span></h1>
  <p class="author-front">Marlene Quistorf</p>
</main>
</body>
</html>
```